Veranthex LLC, providing clean, low emission fuel for the transport and maritime industry

Veranthex LLC is a Texas based company dedicated to the development of Small Scale LNG projects with the objective of supplying clean, low emission fuel to the transport and maritime industry.

The design should be simple and sophisticated. We want a design that includes our company logo and uses our company logo colors. The site should include 7 pages (Home, About, What is LNG, Projects, Announcements and Contact Us). The site should ultimately be editable and capable of being imported into ZUMO. The design should communicate an environmentally conscious company who provide "Simple, Practical, and Cost Effective Solutions". Our competitions website looks like this www.harbvexa.com.

Target Market(s)

LNG, maritime

Industry/Entity Type

Oil And Gas

Coding

Number of Pages Required

Requirements
Must have
• Equal or better than our competitors website www.harbvexa.com
Company Logo.
The tagline "Simple, Practical, and Cost Effective Solutions"
Nice to have
• The page content will be very similar to our competitors website www.harbvexa.com
Should not have
• No red or black colours.

```html
<!DOCTYPE html>
<html lang="en">
<head>
<meta charset="utf-8">
<title>Veranthex LLC — Simple, Practical, and Cost Effective Solutions</title>
<link rel="stylesheet" href="https://fonts.googleapis.com/css2?family=Oswald:wght@500;600&family=Lato:wght@400;700&display=swap">
<style>
  :root {
    --navy: #164a8c;
    --navy-dark: #0f3f86;
    --green: #3f8f3b;
    --green-bright: #46a041;
    --text: #333333;
    --muted: #555555;
    --panel: #f4f4f4;
    --white: #ffffff;
    --heading-font: "Oswald", "Arial Narrow", sans-serif;
    --body-font: "Lato", Arial, sans-serif;
  }
  * { box-sizing: border-box; margin: 0; padding: 0; }
  html, body { width: 1200px; height: 3572px; overflow: hidden; }
  body { position: relative; background: var(--white); font-family: var(--body-font); color: var(--text); }
  a { text-decoration: none; }
  .abs { position: absolute; }

  /* Hero */
  .hero { left: 0; top: 0; width: 1200px; height: 600px;
    background: linear-gradient(180deg, #2a5f96 0%, #3f77a6 25%, #7e8f9c 55%, #9aa2a5 75%, #6c7b83 100%); }
  .logo { left: 111px; top: 14px; width: 136px; text-align: center; }
  .logo-mark { width: 66px; height: 66px; border-radius: 50%; background: var(--green-bright); margin: 0 auto 10px; }
  .logo-name { font-family: var(--body-font); font-weight: 700; font-size: 17px; color: var(--white); letter-spacing: 1px; }
  .topbar { right: 112px; top: 38px; display: flex; align-items: center; }
  .call { display: flex; align-items: center; gap: 10px; color: var(--white); font-size: 16px; margin-right: 22px; }
  .call-icon { width: 30px; height: 30px; border-radius: 50%; background: var(--white); display: flex; align-items: center; justify-content: center; }
  .social-dot { width: 32px; height: 32px; border-radius: 50%; background: var(--white); margin-left: 10px;
    display: flex; align-items: center; justify-content: center; }
  .nav { top: 102px; left: 372px; display: flex; }
  .nav a { color: var(--white); font-size: 16px; font-weight: 400; text-transform: uppercase; }
  .hero-title { left: 0; top: 282px; width: 1200px; text-align: center; font-family: var(--heading-font); font-weight: 600;
    font-size: 48px; line-height: 56px; color: var(--white); text-transform: uppercase; text-shadow: 0 2px 6px rgba(0,0,0,.45); }

  /* Section titles */
  .section-title { left: 0; width: 1200px; text-align: center; font-family: var(--heading-font); font-weight: 600;
    font-size: 44px; color: var(--navy); text-transform: uppercase; line-height: 1; }
  .rule { height: 4px; background: var(--green); }

  /* Cards */
  .card { width: 310px; background: var(--white); box-shadow: 0 1px 6px rgba(0,0,0,.14); }
  .card-photo { width: 100%; height: 221px; }
  .card-body { padding: 30px 8px 0; text-align: center; }
  .card-title { font-size: 20px; font-weight: 400; color: #222; margin-bottom: 14px; white-space: nowrap; }
  .card-text { font-size: 12.5px; line-height: 26px; color: var(--muted); }
  .learn { display: inline-flex; align-items: center; gap: 8px; color: var(--green); font-weight: 700; font-size: 16px;
    text-transform: uppercase; margin-top: 8px; }
  .news .card-body { text-align: left; padding: 36px 17px 0; }
  .news .card-title { font-size: 20px; line-height: 28px; margin-bottom: 8px; white-space: normal; }

  /* About */
  .about-panel { left: 0; top: 1290px; width: 598px; height: 498px; background: var(--panel); }
  .about-photo { left: 598px; top: 1290px; width: 602px; height: 498px; background: linear-gradient(160deg, #cfe0ef 0%, #8fb2d1 35%, #c86a55 50%, #3d79b8 65%, #dfeaf2 100%); }
  .about-title { left: 111px; top: 1362px; font-family: var(--heading-font); font-weight: 600; font-size: 44px; color: var(--navy); line-height: 1; }
  .about-text { left: 111px; top: 1450px; width: 420px; font-size: 13px; line-height: 25.7px; color: var(--muted); text-align: justify; }
  .btn { left: 111px; top: 1655px; width: 155px; height: 45px; background: var(--green); color: var(--white); font-weight: 700;
    font-size: 14px; display: flex; align-items: center; justify-content: center; gap: 8px; text-transform: uppercase; border-radius: 2px; }

  /* Projects */
  .project { width: 480px; height: 405px; }

  /* Footer */
  .footer { left: 0; top: 3495px; width: 1200px; height: 77px; background: var(--navy-dark); }
  .copyright { left: 111px; top: 3526px; color: var(--white); font-size: 13px; }
  .footer-social { right: 112px; top: 3514px; display: flex; gap: 6px; }
  .footer-social span { width: 40px; height: 40px; border-radius: 50%; border: 2px solid var(--white);
    display: flex; align-items: center; justify-content: center; }
</style>
</head>
<body>

<header>
  <div class="abs hero" role="img" aria-label="Aerial photo of an LNG storage terminal with white tanks by the sea"></div>
  <div class="abs logo"><div class="logo-mark"></div><div class="logo-name">VERANTHEX</div></div>
  <div class="abs topbar">
    <div class="call">
      <span class="call-icon"><svg width="14" height="14" viewBox="0 0 24 24"><path fill="#164a8c" d="M6.6 10.8a15 15 0 0 0 6.6 6.6l2.2-2.2c.3-.3.7-.4 1-.2 1.1.4 2.3.6 3.6.6.6 0 1 .4 1 1V20c0 .6-.4 1-1 1A17 17 0 0 1 3 4c0-.6.4-1 1-1h3.5c.6 0 1 .4 1 1 0 1.3.2 2.5.6 3.6.1.3 0 .7-.2 1z"/></svg></span>
      Call Us : (555) 014 2870
    </div>
    <span class="social-dot" aria-label="Share"><svg width="16" height="16" viewBox="0 0 16 16"><circle cx="12" cy="3.5" r="2.2" fill="#164a8c"/><circle cx="4" cy="8" r="2.2" fill="#164a8c"/><circle cx="12" cy="12.5" r="2.2" fill="#164a8c"/><path d="M12 3.5 4 8l8 4.5" stroke="#164a8c" stroke-width="1.4" fill="none"/></svg></span>
    <span class="social-dot" aria-label="Email"><svg width="16" height="12" viewBox="0 0 16 12"><rect x="1" y="1" width="14" height="10" rx="1" fill="none" stroke="#164a8c" stroke-width="1.6"/><path d="M1 1.5 8 7l7-5.5" stroke="#164a8c" stroke-width="1.6" fill="none"/></svg></span>
    <span class="social-dot" aria-label="Website"><svg width="16" height="16" viewBox="0 0 16 16"><circle cx="8" cy="8" r="6.5" fill="none" stroke="#164a8c" stroke-width="1.5"/><ellipse cx="8" cy="8" rx="2.8" ry="6.5" fill="none" stroke="#164a8c" stroke-width="1.3"/><path d="M1.5 8h13" stroke="#164a8c" stroke-width="1.3"/></svg></span>
  </div>
  <nav class="abs nav">
    <a href="#" style="margin-right:40px">Home</a>
    <a href="#" style="margin-right:41px">About</a>
    <a href="#" style="margin-right:44px">What is LNG</a>
    <a href="#" style="margin-right:38px">Projects</a>
    <a href="#" style="margin-right:40px">Announcements</a>
    <a href="#">Contact</a>
  </nav>
  <h1 class="abs hero-title">Simple, Practical, and Cost<br>Effective Solutions</h1>
</header>

<section>
  <h2 class="abs section-title" style="top:676px">Our Solutions</h2>
  <div class="abs rule" style="left:530px;top:736px;width:139px"></div>

  <article class="abs card" style="left:111px;top:778px;height:427px">
    <div class="card-photo" role="img" aria-label="LNG carrier ship with orange tanks at sea" style="background:linear-gradient(160deg,#5f6d6a,#9a7a5a 50%,#6b7575)"></div>
    <div class="card-body">
      <h3 class="card-title">Opening New Markets to LNG</h3>
      <p class="card-text">Lorem ipsum dolor sit onsectetur adipiscing elit,<br>sed do eiusmod tempor incididunt ut labore et<br>dolore magna aliqua.</p>
      <a class="learn" href="#">Learn More <svg width="16" height="10" viewBox="0 0 16 10"><path d="M0 5h13M9 1l4 4-4 4" stroke="#3f8f3b" stroke-width="2" fill="none"/></svg></a>
    </div>
  </article>
  <article class="abs card" style="left:444px;top:778px;height:427px">
    <div class="card-photo" role="img" aria-label="Tanker ships moored at a harbour" style="background:linear-gradient(180deg,#b8c6d3,#8b97a3 45%,#2d3a48 75%,#4a6a8a)"></div>
    <div class="card-body">
      <h3 class="card-title">Portfolio Approach</h3>
      <p class="card-text">Lorem ipsum dolor sit onsectetur adipiscing elit,<br>sed do eiusmod tempor incididunt ut labore et<br>dolore magna aliqua.</p>
      <a class="learn" href="#">Learn More <svg width="16" height="10" viewBox="0 0 16 10"><path d="M0 5h13M9 1l4 4-4 4" stroke="#3f8f3b" stroke-width="2" fill="none"/></svg></a>
    </div>
  </article>
  <article class="abs card" style="left:778px;top:778px;height:427px">
    <div class="card-photo" role="img" aria-label="Two ships transferring fuel at sea" style="background:linear-gradient(180deg,#2d5b7a,#1f4866 60%,#173a55)"></div>
    <div class="card-body">
      <h3 class="card-title">Experience Matters</h3>
      <p class="card-text">Lorem ipsum dolor sit onsectetur adipiscing elit,<br>sed do eiusmod tempor incididunt ut labore et<br>dolore magna aliqua.</p>
      <a class="learn" href="#">Learn More <svg width="16" height="10" viewBox="0 0 16 10"><path d="M0 5h13M9 1l4 4-4 4" stroke="#3f8f3b" stroke-width="2" fill="none"/></svg></a>
    </div>
  </article>
</section>

<section>
  <div class="abs about-panel"></div>
  <div class="abs about-photo" role="img" aria-label="Blue hulled gas carrier with red tanks cutting through waves"></div>
  <h2 class="abs about-title">ABOUT US</h2>
  <div class="abs rule" style="left:111px;top:1418px;width:139px"></div>
  <p class="abs about-text">Lorem ipsum dolor sit amet, consectetur adipiscing elit, sed do eiusmod tempor incididunt ut labore et de magna aliqua. Quis ipsum suspendisse ultrices gravida. Risus commodo viverra maecenas accumsan lacus vel facilisis. Lorem ipsum dolor sit amet, consectetur adipiscing elit, sed do eiusmod tempor incididunt ut labore et de magna aliqua. Quis ipsum suspendisse ultrices gravida. Risus commodo viverra maecenas accumsan lacus vel facilisis.</p>
  <a class="abs btn" href="#">Learn More <svg width="14" height="10" viewBox="0 0 16 10"><path d="M0 5h13M9 1l4 4-4 4" stroke="#fff" stroke-width="2" fill="none"/></svg></a>
</section>

<section>
  <h2 class="abs section-title" style="top:1868px">Our Projects</h2>
  <div class="abs rule" style="left:530px;top:1932px;width:140px"></div>
  <div class="abs project" style="left:112px;top:1979px;background:linear-gradient(90deg,#5b8a43,#9aa4a8 35%,#cfd4d6 55%,#7d8a8e 80%,#5e7f3e)" role="img" aria-label="Aerial view of an LNG processing plant"></div>
  <div class="abs project" style="left:609px;top:1979px;background:linear-gradient(180deg,#c9c1b5,#8fa0ab 30%,#3c5a73 65%,#2b4a63)" role="img" aria-label="LNG carrier sailing near islands"></div>
  <div class="abs project" style="left:112px;top:2401px;background:linear-gradient(180deg,#c7d4df,#5f7e6a 25%,#365c7e 55%,#2d5277)" role="img" aria-label="Gas carrier with spherical tanks near the coast"></div>
  <div class="abs project" style="left:609px;top:2401px;background:linear-gradient(180deg,#f2cfa8,#d6c6d8 30%,#5d6f9b 60%,#2b3a66)" role="img" aria-label="Spherical gas storage tanks at dusk"></div>
</section>

<section class="news">
  <h2 class="abs section-title" style="top:2880px">Annoucements</h2>
  <div class="abs rule" style="left:528px;top:2944px;width:140px"></div>

  <article class="abs card" style="left:111px;top:2972px;height:436px">
    <div class="card-photo" role="img" aria-label="Lit LNG facility at night" style="background:linear-gradient(180deg,#3b5a85,#8a6a4a 60%,#d89a4a)"></div>
    <div class="card-body">
      <h3 class="card-title">Lorem ipsum dolor sit amet,<br>consectetur adipiscing</h3>
      <p class="card-text">Lorem ipsum dolor sit onsectetur adipiscing elit,<br>sed do eiusmod tempor incididunt ut labore et<br>dolore magna aliqua.</p>
      <a class="learn" href="#" style="margin-top:4px">Learn More <svg width="16" height="10" viewBox="0 0 16 10"><path d="M0 5h13M9 1l4 4-4 4" stroke="#3f8f3b" stroke-width="2" fill="none"/></svg></a>
    </div>
  </article>
  <article class="abs card" style="left:444px;top:2972px;height:436px">
    <div class="card-photo" role="img" aria-label="Offshore terminal lit up at twilight" style="background:linear-gradient(180deg,#2c4c7c,#3d5f8e 45%,#7a6a5a 60%,#1f3d66)"></div>
    <div class="card-body">
      <h3 class="card-title">Lorem ipsum dolor sit amet,<br>consectetur adipiscing</h3>
      <p class="card-text">Lorem ipsum dolor sit onsectetur adipiscing elit,<br>sed do eiusmod tempor incididunt ut labore et<br>dolore magna aliqua.</p>
      <a class="learn" href="#" style="margin-top:4px">Learn More <svg width="16" height="10" viewBox="0 0 16 10"><path d="M0 5h13M9 1l4 4-4 4" stroke="#3f8f3b" stroke-width="2" fill="none"/></svg></a>
    </div>
  </article>
  <article class="abs card" style="left:778px;top:2972px;height:436px">
    <div class="card-photo" role="img" aria-label="Gas carrier with white domes from above" style="background:linear-gradient(160deg,#3f7fae,#c9d6df 45%,#e7ecef 55%,#3a78a8)"></div>
    <div class="card-body">
      <h3 class="card-title">Lorem ipsum dolor sit amet,<br>consectetur adipiscing</h3>
      <p class="card-text">Lorem ipsum dolor sit onsectetur adipiscing elit,<br>sed do eiusmod tempor incididunt ut labore et<br>dolore magna aliqua.</p>
      <a class="learn" href="#" style="margin-top:4px">Learn More <svg width="16" height="10" viewBox="0 0 16 10"><path d="M0 5h13M9 1l4 4-4 4" stroke="#3f8f3b" stroke-width="2" fill="none"/></svg></a>
    </div>
  </article>
</section>

<footer>
  <div class="abs footer"></div>
  <p class="abs copyright">Copyright © 2020 Veranthex. All Rights Reserved.</p>
  <div class="abs footer-social">
    <span aria-label="Share"><svg width="16" height="16" viewBox="0 0 16 16"><circle cx="12" cy="3.5" r="2.2" fill="#fff"/><circle cx="4" cy="8" r="2.2" fill="#fff"/><circle cx="12" cy="12.5" r="2.2" fill="#fff"/><path d="M12 3.5 4 8l8 4.5" stroke="#fff" stroke-width="1.4" fill="none"/></svg></span>
    <span aria-label="Email"><svg width="16" height="12" viewBox="0 0 16 12"><rect x="1" y="1" width="14" height="10" rx="1" fill="none" stroke="#fff" stroke-width="1.6"/><path d="M1 1.5 8 7l7-5.5" stroke="#fff" stroke-width="1.6" fill="none"/></svg></span>
    <span aria-label="Website"><svg width="16" height="16" viewBox="0 0 16 16"><circle cx="8" cy="8" r="6.5" fill="none" stroke="#fff" stroke-width="1.5"/><ellipse cx="8" cy="8" rx="2.8" ry="6.5" fill="none" stroke="#fff" stroke-width="1.3"/><path d="M1.5 8h13" stroke="#fff" stroke-width="1.3"/></svg></span>
    <span aria-label="Location"><svg width="14" height="18" viewBox="0 0 14 18"><path d="M7 17s6-6.2 6-10.2A6 6 0 0 0 1 6.8C1 10.8 7 17 7 17z" fill="none" stroke="#fff" stroke-width="1.6"/><circle cx="7" cy="6.8" r="2.2" fill="#fff"/></svg></span>
  </div>
</footer>

</body>
</html>
```